electrical contractor business card for professional modern company

I need a business card design for an electrical contractors business. I do all kinds of electricical work from new homes, air conditioning, data and communications. I have a logo design i want on it and have a good idea in my head of what i want it to look like. I like simple yet bold and professional looking. All black background is a must

Target Market(s)

Anyone needing electrical work done

Industry/Entity Type

Electrical

Contact Information for Business Card

company name- KTW Electrical and Data
person name-martin pellowe
phone number- 0418 362 927
website-ktwelec.example.com.au

Font styles to use
Sans Serif

Requirements
Must have
• email
• website
• logo
• name
• phone number
• list of work i do:
• -electrical
• -air-conditioning
• -data/communications
• -cctv/security
• -domestic/commercial/industrial
• -24hr emergency breakdown repair
Nice to have
• i would like the logo on the front side in the centre taking up most of the card with black background.
• on the rear i want the list of work i do with company info i.e. email, website, my name, phone number. rear of card also black background with orange writing to match the orange in the logo

```html
<!DOCTYPE html>
<html lang="en">
<head>
<meta charset="utf-8">
<title>KTW Electrical and Data – Business Card</title>
<link href="https://fonts.googleapis.com/css2?family=Montserrat:wght@400;500;600;700&display=swap" rel="stylesheet">
<style>
  :root {
    --page-bg: #d9d9d7;
    --card-black: #161616;
    --brand-orange: #e8692a;
    --orange-glow: #f07a35;
    --rule-dark: #050505;
  }
  * { margin: 0; padding: 0; box-sizing: border-box; }
  html, body {
    width: 1200px;
    height: 900px;
    overflow: hidden;
  }
  body {
    background: var(--page-bg);
    font-family: "Montserrat", Arial, sans-serif;
    position: relative;
  }
  .card {
    position: absolute;
    width: 540px;
    height: 300px;
    background: var(--card-black);
    border-radius: 3px;
    box-shadow: 0 14px 30px rgba(0,0,0,0.35);
    overflow: hidden;
  }
  /* Front */
  .card-front {
    left: 90px;
    top: 110px;
    display: flex;
    align-items: center;
    justify-content: center;
  }
  .brand-lockup {
    display: flex;
    align-items: center;
    gap: 14px;
  }
  .brand-square {
    width: 14px;
    height: 14px;
    background: var(--brand-orange);
  }
  .brand-name {
    color: var(--brand-orange);
    font-weight: 500;
    font-size: 24px;
    letter-spacing: 0.3px;
  }
  /* Back */
  .card-back {
    left: 570px;
    top: 490px;
  }
  .services-band {
    position: absolute;
    left: 0;
    right: 0;
    top: 34px;
    height: 112px;
  }
  .band-rule {
    position: absolute;
    left: 0;
    right: 0;
    height: 3px;
    background: linear-gradient(90deg, var(--rule-dark) 0%, var(--brand-orange) 45%, var(--orange-glow) 60%, var(--rule-dark) 100%);
  }
  .band-rule.top { top: 0; }
  .band-rule.bottom { bottom: 0; }
  .service-list {
    list-style: none;
    position: absolute;
    inset: 16px 26px 16px 26px;
    color: var(--brand-orange);
    font-size: 11.5px;
    font-weight: 400;
    letter-spacing: 0.8px;
    text-transform: uppercase;
  }
  .service-list li { position: absolute; white-space: nowrap; }
  .svc-aircon { left: 110px; top: 2px; }
  .svc-data { right: 0; top: 2px; }
  .svc-electrical { left: 0; top: 28px; }
  .svc-sectors { right: 8px; top: 28px; }
  .svc-cctv { left: 24px; top: 54px; }
  .svc-emergency { left: 160px; top: 54px; }

  .contact-name {
    position: absolute;
    left: 26px;
    top: 196px;
    color: var(--brand-orange);
    font-weight: 700;
    font-size: 22px;
    letter-spacing: 1px;
    text-transform: uppercase;
  }
  .contact-web {
    position: absolute;
    right: 22px;
    top: 168px;
  }
  .contact-row {
    position: absolute;
    left: 26px;
    right: 22px;
    bottom: 26px;
    display: flex;
    gap: 28px;
  }
  .contact-item {
    display: flex;
    align-items: center;
    gap: 7px;
    color: var(--brand-orange);
    font-size: 12.5px;
    font-weight: 500;
    letter-spacing: 0.6px;
    text-transform: uppercase;
    white-space: nowrap;
  }
  .contact-icon {
    width: 14px;
    height: 14px;
    flex: none;
  }
</style>
</head>
<body>

  <section class="card card-front" aria-label="Card front">
    <div class="brand-lockup">
      <span class="brand-square"></span>
      <span class="brand-name">KTW Electrical and Data</span>
    </div>
  </section>

  <section class="card card-back" aria-label="Card back">
    <div class="services-band">
      <div class="band-rule top"></div>
      <ul class="service-list">
        <li class="svc-aircon">Air-Conditioning</li>
        <li class="svc-data">Data/Communications</li>
        <li class="svc-electrical">Electrical</li>
        <li class="svc-sectors">Domestic/Commercial/Industrial</li>
        <li class="svc-cctv">CCTV/Security</li>
        <li class="svc-emergency">24HR Emergency Breakdown Repair</li>
      </ul>
      <div class="band-rule bottom"></div>
    </div>

    <div class="contact-item contact-web">
      <svg class="contact-icon" viewBox="0 0 16 16" aria-hidden="true">
        <circle cx="8" cy="8" r="8" fill="var(--brand-orange)"/>
        <path d="M4 8.5 8 4.8l4 3.7V12H9.5V9.5h-3V12H4z" fill="var(--card-black)"/>
      </svg>
      <span>ktwelec.example.com.au</span>
    </div>

    <h2 class="contact-name">Martin Pellowe</h2>

    <div class="contact-row">
      <div class="contact-item">
        <svg class="contact-icon" viewBox="0 0 16 16" aria-hidden="true">
          <circle cx="8" cy="8" r="8" fill="var(--brand-orange)"/>
          <path d="M5.2 4.2c.4-.3.9-.2 1.1.2l.7 1.3c.2.4.1.8-.2 1l-.5.4c.4.9 1.1 1.6 2 2l.4-.5c.3-.3.7-.4 1-.2l1.3.7c.4.2.5.7.2 1.1l-.6.7c-.4.4-1 .5-1.6.3C7 10.5 5.5 9 4.8 7c-.2-.6-.1-1.2.3-1.6z" fill="var(--card-black)"/>
        </svg>
        <span>0418 362 927</span>
      </div>
      <div class="contact-item">
        <svg class="contact-icon" viewBox="0 0 16 16" aria-hidden="true">
          <circle cx="8" cy="8" r="7" fill="none" stroke="var(--brand-orange)" stroke-width="1.6"/>
          <rect x="4.5" y="5.5" width="7" height="5" fill="none" stroke="var(--brand-orange)" stroke-width="1.1"/>
          <path d="M4.5 5.5 8 8.3l3.5-2.8" fill="none" stroke="var(--brand-orange)" stroke-width="1.1"/>
        </svg>
        <span>martin@ktwelec.example.com.au</span>
      </div>
    </div>
  </section>

</body>
</html>
```